New, modern business card for growing audiology practice

We need a new business card for our audiology practice. Our logo and website have recently changed (more modern) and we want our business cards to reflect this change.
We conduct hearing tests, perform earwax removals, and fit & dispense hearing aids to our patients. We are a family owned practice in which the owner is the one who works directly with the patient. I have attached logos in various formats to use, as well as two ideas I found on this website; as well as a scanned copy of our current logo. Good luck!

Industry/Entity Type

Business

Contact Information for Business Card

Company name: Birchmont Hearing Center
Provider name: Peter Lowsby, Au.D. F/NSO
Phone number: (555) 318-6042
Address: 287 W. Hollister Rd. Larkfield, KY 40000
email: birchmonthearing@quillpost.net
website: birchmonthearing.net

Colors
000000
aaaaaa
dbdbdb
cacaca
9bcb3c
afd23c
cadf82
b1b1b1

Requirements
Must have
• My card must include information in the "details" section. In the attached images, I found a few that I liked and I would like to model after - "steady strivin'" and "Sound Lab Clinic".
• Must be horizontal.
• Must include logos provided. I uploaded them in various file formats and various ways.
• Must match logo font, if possible, if not, please get as close as you can.
Nice to have
• I really like the idea of having a color on one side with just the logo and company name and the contact information and provider name on the other side. I also really like the idea of having the main color dominating on the logo/company side with accent of that same color on the contact side of the card.
Should not have
• Must not be vertical.

```html
<!DOCTYPE html>
<html lang="en">
<head>
<meta charset="utf-8">
<title>Birchmont Hearing Center – Business Card</title>
<link href="https://fonts.googleapis.com/css2?family=Cabin:wght@400&family=Roboto:wght@400&family=Roboto+Condensed:wght@700&display=swap" rel="stylesheet">
<style>
  :root {
    --backdrop: #e9e9e6;
    --card-light: #fbfbfa;
    --card-dark: #1b1c1e;
    --brand-green: #7aa83f;
    --ink: #111111;
    --ink-soft: #555555;
    --divider: #cacaca;
    --white: #ffffff;
  }
  * { margin: 0; padding: 0; box-sizing: border-box; }
  html, body {
    width: 1200px; height: 960px; overflow: hidden;
    background: var(--backdrop);
  }
  .canvas { position: relative; width: 1200px; height: 960px; }

  .card {
    position: absolute;
    width: 600px; height: 343px;
    border-radius: 22px;
  }
  .card--front { left: 314px; top: 113px; background: var(--card-light); }
  .card--back  { left: 311px; top: 472px; background: var(--card-dark); }

  .brand {
    position: absolute;
    display: flex; align-items: center;
    font-family: "Cabin", sans-serif;
    font-weight: 400;
    white-space: nowrap;
  }
  .brand__dot { border-radius: 50%; background: var(--brand-green); flex: none; }

  .card--front .brand {
    left: 0; right: 0; top: 84px; justify-content: center;
    font-size: 26px; letter-spacing: 0.2px; color: var(--ink);
  }
  .card--front .brand__dot { width: 18px; height: 18px; margin-right: 12px; }

  .provider {
    position: absolute; right: 358px; top: 204px; text-align: right;
    font-family: "Roboto Condensed", sans-serif; font-weight: 700;
  }
  .provider__name { font-size: 21px; color: var(--brand-green); line-height: 1.15; }
  .provider__creds { font-size: 15px; color: var(--ink); margin-top: 3px; }

  .divider {
    position: absolute; left: 270px; top: 174px;
    width: 1px; height: 108px; background: var(--divider);
  }

  .contact {
    position: absolute; left: 297px; top: 175px;
    font-family: "Roboto", sans-serif; font-size: 14px; color: var(--ink-soft);
    line-height: 18px; list-style: none;
  }
  .contact__address { margin-bottom: 11px; }
  .contact__row { display: flex; align-items: center; }
  .contact__icon { width: 12px; height: 12px; margin-right: 11px; fill: var(--brand-green); flex: none; }

  .card--back .brand {
    left: 0; right: 0; top: 150px; justify-content: center;
    font-size: 30px; color: var(--brand-green);
  }
  .card--back .brand__dot { width: 22px; height: 22px; margin-right: 14px; }

  .web-address {
    position: absolute; left: 0; right: 0; top: 294px; text-align: center;
    font-family: "Roboto", sans-serif; font-size: 14px;
    letter-spacing: 3.2px; color: var(--white);
  }
</style>
</head>
<body>
<main class="canvas">
  <section class="card card--front" aria-label="Card front">
    <div class="brand"><span class="brand__dot"></span>BIRCHMONT HEARING CENTER</div>

    <div class="provider">
      <p class="provider__name">PETER LOWSBY</p>
      <p class="provider__creds">AU.D. F/NSO</p>
    </div>

    <div class="divider"></div>

    <ul class="contact">
      <li class="contact__address">287 W. Hollister Rd.<br>Larkfield, KY 40000</li>
      <li class="contact__row">
        <svg class="contact__icon" viewBox="0 0 24 24" aria-hidden="true"><path d="M6.6 10.8c1.4 2.8 3.8 5.1 6.6 6.6l2.2-2.2c.3-.3.7-.4 1-.2 1.1.4 2.3.6 3.6.6.6 0 1 .4 1 1V20c0 .6-.4 1-1 1C10.6 21 3 13.4 3 4c0-.6.4-1 1-1h3.5c.6 0 1 .4 1 1 0 1.3.2 2.5.6 3.6.1.3 0 .7-.2 1z"/></svg>
        (555) 318-6042
      </li>
      <li class="contact__row">
        <svg class="contact__icon" viewBox="0 0 24 24" aria-hidden="true"><rect x="1" y="4" width="22" height="16"/><path d="M1.5 5l10.5 8 10.5-8" stroke="#ffffff" stroke-width="2" fill="none"/></svg>
        birchmonthearing@quillpost.net
      </li>
      <li class="contact__row">
        <svg class="contact__icon" viewBox="0 0 24 24" aria-hidden="true"><circle cx="12" cy="12" r="11"/><path d="M7 7c2 0 3 1 3 3s-2 2-2 4 2 3 2 5M15 4c0 2 2 3 3 3M14 13c1 0 2 1 2 3" stroke="#ffffff" stroke-width="1.8" fill="none"/></svg>
        birchmonthearing.net
      </li>
    </ul>
  </section>

  <section class="card card--back" aria-label="Card back">
    <div class="brand"><span class="brand__dot"></span>BIRCHMONT HEARING CENTER</div>
    <p class="web-address">www.birchmonthearing.net</p>
  </section>
</main>
</body>
</html>
```